Website - Corla Bastwick

I need a website that has multiple pages and easy for me to update pictures, content and blogs as an ongoing basis’s.
It will have videos and needs to be compatible to view easily and aesthetically on mobile phones.
Please refer to this website for inspiration www.velquistorin.com

Coding

Coded - Design and coding required

Number of Pages Required

5+ page

Font styles to use
Other font styles liked:
• Refer to website provided as inspiration

Requirements
Must have
• Please use stock images for now to do design, but I will be providing all imagery, videos and content

```html
<!DOCTYPE html>
<html lang="en">
<head>
<meta charset="utf-8">
<title>Corla Bastwick</title>
<link rel="stylesheet" href="https://fonts.googleapis.com/css2?family=Lora:wght@400;500&family=IBM+Plex+Sans:wght@400;500&display=swap">
<style>
  :root {
    --cream: #f5ebe6;
    --tan: #dbc1b2;
    --ink: #1a1717;
    --dark: #1e1a1a;
    --white: #ffffff;
    --text: #3a3434;
    --muted: #5b5353;
  }
  * { box-sizing: border-box; margin: 0; padding: 0; }
  html, body { width: 1200px; height: 2924px; overflow: hidden; }
  body {
    position: relative;
    background: var(--cream);
    font-family: "IBM Plex Sans", sans-serif;
    color: var(--text);
  }
  .abs { position: absolute; }
  .serif { font-family: "Lora", serif; font-weight: 400; }

  /* hero */
  .hero { left: 0; top: 0; width: 1200px; height: 641px; overflow: hidden; }
  .hero-photo-left { left: 0; top: 0; width: 592px; height: 641px;
    background: linear-gradient(180deg, #2a2a2a 0%, #4a4a4a 40%, #6a6a6a 70%, #3c3c3c 100%); }
  .hero-photo-right { left: 592px; top: 0; width: 608px; height: 641px;
    background: linear-gradient(180deg, #262626 0%, #555 35%, #7a7a7a 65%, #454545 100%); }
  .hero-shade { left: 0; top: 0; width: 1200px; height: 641px; background: rgba(0,0,0,0.28); }
  .brand { left: 144px; top: 30px; font-size: 42px; color: var(--white); letter-spacing: 0.3px; white-space: nowrap; }
  .nav { top: 44px; font-size: 18px; color: var(--white); white-space: nowrap; }
  .nav-active { border-bottom: 3px solid var(--tan); padding-bottom: 8px; }
  .nav-social { left: 1038px; top: 47px; width: 18px; height: 18px; border: 2px solid var(--white); border-radius: 50%; }
  .hero-center { left: 0; top: 302px; width: 1200px; display: flex; flex-direction: column; align-items: center; }
  .hero-title { height: 97px; padding: 0 42px; background: var(--white); white-space: nowrap;
    display: flex; align-items: center; justify-content: center; font-size: 60px; line-height: 1; color: var(--ink); }
  .hero-btn { width: 163px; height: 49px; background: var(--tan); white-space: nowrap;
    display: flex; align-items: center; justify-content: center; font-size: 18px; color: var(--ink); }

  /* about */
  .about-photo { left: 143px; top: 704px; width: 428px; height: 505px;
    background: linear-gradient(135deg, #e9e9ea 0%, #c9a690 45%, #7a5140 70%, #e4e4e6 100%); }
  .about-kicker { left: 650px; top: 730px; font-size: 64px; color: var(--ink); line-height: 1.1; white-space: nowrap; }
  .about-name { left: 650px; top: 805px; font-size: 50px; color: var(--ink); line-height: 1.1; white-space: nowrap; }
  .about-copy { left: 650px; top: 886px; width: 410px; font-size: 15px; line-height: 27.3px; color: var(--muted); }
  .btn-dark { left: 650px; top: 1118px; width: 164px; height: 48px; background: var(--ink); color: var(--white);
    display: flex; align-items: center; justify-content: center; font-size: 18px; }

  /* videos */
  .videos { left: 0; top: 1281px; width: 1200px; height: 533px; background: var(--tan); }
  .section-title { width: 1200px; left: 0; text-align: center; font-size: 50px; color: var(--ink); white-space: nowrap; }
  .video-thumb { top: 1472px; width: 294px; height: 205px; display: flex; align-items: center; justify-content: center; }
  .thumb-a { left: 144px; background: linear-gradient(90deg, #1c1a1a 0%, #c8c2bb 30%, #2a2220 55%, #ddd6cf 80%, #1a1818 100%); }
  .thumb-b { left: 453px; background: linear-gradient(90deg, #e8e6e4 0%, #b98a6e 40%, #d66ba0 60%, #e9e7e6 100%); }
  .thumb-c { left: 763px; background: linear-gradient(180deg, #5b6b4a 0%, #3a5d84 45%, #2d4f78 75%, #a8bfd9 100%); }
  .video-caption { top: 1698px; width: 294px; text-align: center; font-size: 18px; font-weight: 500; color: #3a302c; }

  /* blogs */
  .blog-photo { top: 2012px; width: 444px; height: 310px; }
  .blog-a { left: 144px; background: linear-gradient(135deg, #e2e2e2 0%, #8a8a8a 45%, #2a2a2a 70%, #d4d4d4 100%); }
  .blog-b { left: 611px; background: linear-gradient(135deg, #7a3a2c 0%, #b6785c 40%, #d58aa0 70%, #3a2522 100%); }
  .blog-title { top: 2346px; width: 400px; font-size: 20px; line-height: 28px; font-weight: 500; color: #3a302c; }
  .blog-date { top: 2413px; font-size: 13px; color: var(--muted); }

  /* footer */
  .footer { left: 0; top: 2508px; width: 1200px; height: 416px; background: var(--dark); }
  .field { top: 2654px; height: 40px; background: var(--white); font-size: 13px; color: #6a6262;
    display: flex; align-items: center; padding-left: 20px; }
  .submit { left: 855px; top: 2654px; width: 122px; height: 40px; background: var(--tan); color: var(--ink);
    font-size: 15px; display: flex; align-items: center; justify-content: center; }
  .social { top: 2738px; width: 46px; height: 46px; border-radius: 50%; background: var(--white); color: var(--ink);
    font-size: 8px; display: flex; align-items: center; justify-content: center; text-align: center; }
  .footer-nav { left: 0; top: 2811px; width: 1200px; text-align: center; font-size: 18px; color: var(--white); white-space: nowrap; }
  .footer-nav span { margin: 0 22px; }
  .legal { left: 0; top: 2857px; width: 1200px; text-align: center; font-size: 13px; color: var(--white); white-space: nowrap; }
</style>
</head>
<body>

<section class="abs hero">
  <div class="abs hero-photo-left" role="img" aria-label="Black and white photo of a woman in a dress on a wooden jetty by the water"></div>
  <div class="abs hero-photo-right" role="img" aria-label="Black and white photo of a woman sitting on a jetty with boats behind"></div>
  <div class="abs hero-shade"></div>
  <div class="abs brand serif">Corla Bastwick</div>
  <div class="abs nav nav-active" style="left:606px;">Home</div>
  <div class="abs nav" style="left:690px;">About</div>
  <div class="abs nav" style="left:774px;">Blogs</div>
  <div class="abs nav" style="left:855px;">Videos</div>
  <div class="abs nav" style="left:946px;">Contact</div>
  <div class="abs nav-social" aria-label="Snapfold"></div>
  <div class="abs hero-center">
    <h1 class="hero-title serif">CORLA BASTWICK</h1>
    <div class="hero-btn">GET STARTED</div>
  </div>
</section>

<section>
  <div class="abs about-photo" role="img" aria-label="Portrait photo of a smiling woman with long brown hair"></div>
  <h2 class="abs about-kicker serif">ABOUT</h2>
  <div class="abs about-name serif">Corla Bastwick</div>
  <p class="abs about-copy">Lorem ipsum dolor sit amet, consectetur adipiscing elied do eiusmod tempor incididunt ut labore et dolore magna aliquis ipsum suspendisse ultrices gravidisus commodo viverra maecenas accumsan lacus vel facilisisorem ipsum dolor sit amet, consectetur adipiscing elied do eiusmod tempor incididunt ut labore et dolore magna aliquuis ipsum suspendisse ultrices gravidisus commodo</p>
  <div class="abs btn-dark">READ MORE</div>
</section>

<section class="abs videos"></section>
<h2 class="abs section-title serif" style="top:1362px;">LATEST VIDEOS</h2>
<div class="abs video-thumb thumb-a" role="img" aria-label="Video still of a woman against a striped backdrop">
  <svg width="80" height="80" viewBox="0 0 80 80"><circle cx="40" cy="40" r="36" fill="none" stroke="#fff" stroke-width="6"/><path d="M32 25 L57 40 L32 55 Z" fill="#fff"/></svg>
</div>
<div class="abs video-thumb thumb-b" role="img" aria-label="Video still of a woman in a pink top indoors">
  <svg width="80" height="80" viewBox="0 0 80 80"><circle cx="40" cy="40" r="36" fill="none" stroke="#fff" stroke-width="6"/><path d="M32 25 L57 40 L32 55 Z" fill="#fff"/></svg>
</div>
<div class="abs video-thumb thumb-c" role="img" aria-label="Video still of a woman sitting by a lake">
  <svg width="80" height="80" viewBox="0 0 80 80"><circle cx="40" cy="40" r="36" fill="none" stroke="#fff" stroke-width="6"/><path d="M32 25 L57 40 L32 55 Z" fill="#fff"/></svg>
</div>
<div class="abs video-caption" style="left:144px;">Lorem ipsum dolor sit</div>
<div class="abs video-caption" style="left:453px;">Duis aute irure dolor</div>
<div class="abs video-caption" style="left:763px;">Ut enim ad minim eniam</div>

<h2 class="abs section-title serif" style="top:1904px;">LATEST BLOGS</h2>
<div class="abs blog-photo blog-a" role="img" aria-label="Black and white photo of a woman in cowboy boots leaning back"></div>
<div class="abs blog-photo blog-b" role="img" aria-label="Collage photo of a woman against vintage magazine pages"></div>
<div class="abs blog-title" style="left:144px;">Sed ut perspiciatis unde omnis iste natus error sit voluptatem</div>
<div class="abs blog-title" style="left:611px;">Sed ut perspiciatis unde omnis iste natus error sit voluptatem</div>
<div class="abs blog-date" style="left:144px;">April 23,2021</div>
<div class="abs blog-date" style="left:611px;">April 23,2021</div>

<footer class="abs footer"></footer>
<h2 class="abs section-title serif" style="top:2553px; color:var(--white);">SUBSCRIPTION</h2>
<div class="abs field" style="left:223px; width:301px;">Full Name</div>
<div class="abs field" style="left:540px; width:301px;">Email Address</div>
<div class="abs submit">SUBMIT</div>
<div class="abs social" style="left:491px;">Loopa</div>
<div class="abs social" style="left:545px;">Chirrup</div>
<div class="abs social" style="left:599px;">Vidora</div>
<div class="abs social" style="left:653px;">Snapfold</div>
<nav class="abs footer-nav">HOME<span>/</span>ABOUT<span>/</span>BLOGS<span>/</span>VIDEOS<span>/</span>CONTACT</nav>
<div class="abs legal">Corla Bastwick © 2021 All rights reserved &nbsp;| Privacy Policy &nbsp;| &nbsp;Terms</div>

</body>
</html>
```